Redesign of Engineering firm website

I want a redesign of the torvelpower.com website with the below in mind:

1- the client has a 3 main sectors: Renewable Energy, Process Automation and General Engineering.
2- Home page should show the 3 sectors
3- the other standard pages should be home, About, Clients, Projects, Training, Career, and Contact
4- The theme should be wordpress.
5- Responsive layout that works with all devices
6- One page layout is preferable for the home page.
7- it should be original and is not copied from other templates.
Updates

Reason: As requested from so many designers... the deadline is extended. Thank you

Target Market(s)

Engineers and professional

Industry/Entity Type

Solar Energy

Font styles to use
Serif
Sans Serif

Colors
3277b5
0355a3
0493ce

Requirements
Must have
• pictures that represent the three sectors

```html
<!DOCTYPE html>
<html lang="en">
<head>
<meta charset="utf-8">
<title>Torvel Power – Renewable Energy, Process Automation and General Engineering</title>
<link rel="stylesheet" href="https://fonts.googleapis.com/css2?family=Bebas+Neue&family=Roboto:ital,wght@0,300;0,400;0,500;0,700;1,400&display=swap">
<style>
:root{
  --teal:#0a84a6;
  --teal-dark:#06708f;
  --ink:#222;
  --text:#777;
  --grey-bg:#efefef;
  --footer:#1f1f1f;
  --footer-text:#cfcfcf;
  --white:#fff;
}
*{box-sizing:border-box;margin:0;padding:0}
html,body{width:1200px;height:3579px;overflow:hidden}
body{font-family:"Roboto",sans-serif;color:var(--ink);background:var(--white);position:relative}
section,header,footer,div{position:relative}
.abs{position:absolute}
.btn{position:absolute;display:flex;align-items:center;justify-content:center;background:var(--teal);color:var(--white);font-size:21px;text-transform:uppercase;border-radius:3px}
.accent{color:var(--teal)}
.section-title{position:absolute;left:0;right:0;text-align:center;font-size:43px;font-weight:400;text-transform:uppercase;letter-spacing:.5px}

/* top bar */
.topbar{height:43px;background:var(--teal);color:var(--white);font-size:15px}
.topbar ul{list-style:none;position:absolute;right:60px;top:0;height:43px;display:flex;align-items:center;gap:36px}
.topbar li{display:flex;align-items:center;gap:10px}

/* header */
.site-header{height:93px;background:var(--white)}
.brand{position:absolute;left:79px;top:18px;display:flex;align-items:center;gap:12px;font-size:44px;font-weight:700;color:var(--teal);letter-spacing:1px}
.brand .dot{width:16px;height:16px;background:var(--teal);border-radius:50%}
.main-nav{position:absolute;right:56px;top:22px;display:flex;gap:6px;list-style:none;font-size:17px;text-transform:uppercase;color:#444}
.main-nav li{padding:14px 12px}
.main-nav li.active{background:var(--teal);color:var(--white);border-radius:3px;padding:14px 26px}

/* hero */
.hero{height:539px;overflow:hidden}
.hero-photo{position:absolute;inset:0;background:linear-gradient(160deg,#9ec4de 0%,#6a94b8 30%,#2f5a86 60%,#1c3555 100%)}
.hero h1{position:absolute;left:0;right:0;top:130px;text-align:center;font-family:"Bebas Neue",sans-serif;font-weight:400;font-size:78px;line-height:76px;color:var(--white);letter-spacing:1px}
.hero .tagline{position:absolute;left:0;right:0;top:301px;text-align:center;font-style:italic;font-size:21px;color:var(--white)}
.hero .arrow{position:absolute;top:240px}

/* welcome */
.welcome{height:597px}
.intro{position:absolute;left:140px;right:140px;top:118px;text-align:center;font-size:15px;line-height:27px;color:var(--text)}
.sector{position:absolute;top:236px;width:300px;text-align:center}
.sector .icon{width:167px;height:167px;margin:0 auto;border-radius:50%;background:#f4f4f4;border:5px solid #e3e3e3;display:flex;align-items:center;justify-content:center}
.sector .icon.featured{background:var(--teal);border-color:#d4eaf1}
.sector h3{margin-top:34px;font-size:21px;font-weight:400;color:var(--teal);text-transform:uppercase}
.sector p{margin-top:12px;font-size:14.5px;line-height:24px;color:var(--text);padding:0 10px}

/* about */
.about{height:453px;background:var(--grey-bg)}
.about h2{position:absolute;left:79px;top:56px;font-size:43px;font-weight:400;text-transform:uppercase}
.about .copy{position:absolute;left:79px;width:515px;top:125px;font-size:15px;line-height:27px;color:#555}
.about .copy p+p{margin-top:10px}
.about-photo{position:absolute;left:620px;top:58px;width:430px;height:321px;border-radius:48% 40% 40% 48%/50% 46% 46% 50%;background:linear-gradient(180deg,#bcd9ef 0%,#5d8fbf 45%,#2d4f73 70%,#5f9a3c 100%)}

/* projects */
.projects{height:554px;background:var(--teal);color:var(--white)}
.projects h2{top:56px;color:#222}
.projects h2 span{color:var(--white)}
.projects .sub{position:absolute;left:0;right:0;top:123px;text-align:center;font-style:italic;font-size:16px}
.card{position:absolute;top:172px;width:322px;background:var(--white)}
.card .photo{height:260px}
.card .title{height:62px;display:flex;align-items:center;padding-left:16px;font-size:18px;color:#444;text-transform:uppercase}
.card.active .title{background:#eeeeee;color:var(--teal)}

/* training & testimonials */
.split{height:501px;background:var(--white)}
.split h2{position:absolute;top:70px;font-size:40px;font-weight:400;text-transform:uppercase}
.divider{position:absolute;left:584px;top:50px;width:18px;height:400px;background:linear-gradient(90deg,rgba(0,0,0,.06),rgba(0,0,0,0))}
.training-photo{position:absolute;left:79px;top:145px;width:465px;height:143px;background:linear-gradient(180deg,#b7cfe4 0%,#d9e3ea 45%,#7f9a6b 70%,#45556a 100%)}
.training-text{position:absolute;left:79px;top:313px;width:480px;font-size:14.5px;line-height:23px;color:var(--text)}
.quote{position:absolute;left:623px;width:480px}
.quote .avatar{position:absolute;left:0;top:0;width:105px;height:105px;border-radius:50%;border:4px solid #e8e8e8;background:linear-gradient(160deg,#d9dfe6,#9aa8b5)}
.quote blockquote{position:absolute;left:119px;top:4px;width:360px;font-style:italic;font-size:15px;line-height:24px;color:var(--text)}
.quote cite{position:absolute;left:119px;top:83px;font-style:italic;font-weight:500;font-size:15px;color:var(--teal)}
.quote .rule{position:absolute;left:52px;top:108px;width:480px;height:2px;background:var(--teal)}
.quote .rule::after{content:"";position:absolute;right:-6px;top:-6px;width:14px;height:14px;border-radius:50%;background:var(--teal)}
.quote .rule::before{content:"";position:absolute;left:0;top:-4px;width:2px;height:6px;background:var(--teal)}

/* contact */
.contact{height:453px;background:var(--white)}
.contact h2{top:65px}
.contact .sub{position:absolute;left:0;right:0;top:120px;text-align:center;font-size:16px;color:var(--text)}
.field{position:absolute;border:1px solid #cfcfcf;background:var(--white);font-size:14px;color:#888;padding:14px 14px}
.contact .btn{left:515px;top:334px;width:167px;height:57px}

/* footer */
.site-footer{height:279px;background:var(--footer);color:var(--footer-text);font-size:15px}
.footer-brand{position:absolute;left:79px;top:70px;display:flex;align-items:center;gap:12px;font-size:46px;font-weight:700;color:var(--teal)}
.footer-brand .dot{width:16px;height:16px;background:var(--teal);border-radius:50%}
.social{position:absolute;top:173px;display:flex;gap:12px;left:124px}
.social span{width:45px;height:45px;border-radius:50%;background:var(--teal)}
.footer-col{position:absolute;top:30px}
.footer-col h4{font-size:18px;font-weight:500;color:var(--teal);text-transform:uppercase;margin-bottom:18px}
.links{list-style:none;line-height:23.2px}
.links li::before{content:"›";color:var(--teal);margin-right:18px;font-size:18px}
.newsletter p{width:250px;line-height:24px}
.newsletter .email{margin-top:12px;width:250px;height:46px;background:var(--white);color:#555;font-size:14px;padding:14px 10px}
.newsletter .btn{position:relative;margin-top:10px;width:158px;height:51px;font-size:20px}
.touch li{list-style:none;display:flex;gap:16px;line-height:24px}
.touch li+li{margin-top:10px}
.touch .name{color:var(--teal)}
.bottom-bar{height:67px;background:var(--teal);color:var(--white);font-size:15px;display:flex;align-items:center;justify-content:center}
</style>
</head>
<body>

<div class="topbar">
  <ul>
    <li>
      <svg width="18" height="18" viewBox="0 0 24 24" fill="none" stroke="#fff" stroke-width="2"><path d="M5 3h4l2 5-3 2a12 12 0 0 0 6 6l2-3 5 2v4a2 2 0 0 1-2 2A17 17 0 0 1 3 5a2 2 0 0 1 2-2z"/></svg>
      info@torvelpower.com
    </li>
    <li>
      <svg width="20" height="16" viewBox="0 0 24 18" fill="none" stroke="#fff" stroke-width="2"><rect x="1" y="1" width="22" height="16" rx="2"/><path d="M1 2l11 8 11-8"/></svg>
      +966135550199
    </li>
    <li>
      <svg width="14" height="18" viewBox="0 0 14 18" fill="#fff"><rect x="0" y="7" width="14" height="11" rx="2"/><path d="M3 7V5a4 4 0 0 1 8 0v2" fill="none" stroke="#fff" stroke-width="2"/></svg>
      Login
    </li>
  </ul>
</div>

<header class="site-header">
  <div class="brand"><span class="dot"></span>TORVEL</div>
  <ul class="main-nav">
    <li class="active">Home</li><li>About</li><li>Services</li><li>Clients</li><li>Projects</li><li>Training</li><li>Career</li><li>Contact</li>
  </ul>
</header>

<section class="hero">
  <div class="hero-photo" role="img" aria-label="Rows of solar panels under a bright cloudy blue sky"></div>
  <h1>We know how to reduce your energy<br>consumption</h1>
  <p class="tagline">Renewable Energy, Process Automation and General Engineering</p>
  <div class="btn" style="left:428px;top:348px;width:164px;height:56px">Know more</div>
  <div class="btn" style="left:606px;top:348px;width:167px;height:56px">Contact us</div>
  <svg class="arrow" style="left:22px" width="22" height="60" viewBox="0 0 22 60"><path d="M20 2L3 30l17 28" fill="none" stroke="rgba(255,255,255,.8)" stroke-width="2"/></svg>
  <svg class="arrow" style="right:22px" width="22" height="60" viewBox="0 0 22 60"><path d="M2 2l17 28L2 58" fill="none" stroke="rgba(255,255,255,.8)" stroke-width="2"/></svg>
</section>

<section class="welcome">
  <h2 class="section-title" style="top:62px">Welcome <span class="accent">Torvel Power</span></h2>
  <p class="intro">We are the solar experts in the solar kingdom. The KSA (Saudi Arabia) solar market is a promising market with huge potential. The plan is to build 41,000 MW of solar in the coming 20 years, as announced by N.R.A (National Renewables Authority). We provide our services, both by our in-house team and associated partners</p>

  <div class="sector" style="left:89px">
    <div class="icon">
      <svg width="80" height="80" viewBox="0 0 80 80" fill="none" stroke="#0a84a6" stroke-width="4"><path d="M28 46a18 18 0 1 1 24 0v8H28z"/><path d="M30 62h20M32 70h16"/><path d="M40 4v6M12 16l5 5M68 16l-5 5M4 36h6M76 36h-6"/></svg>
    </div>
    <h3>Renewable Energy</h3>
    <p>Lorem Ipsum is simply dummy text of the printing and typesetting industry. Lorem Ipsum has been the industry's standard.</p>
  </div>
  <div class="sector" style="left:447px">
    <div class="icon featured">
      <svg width="84" height="84" viewBox="0 0 84 84" fill="none" stroke="#fff" stroke-width="5" stroke-linecap="round"><path d="M14 76h34"/><path d="M31 74V54l20-22"/><circle cx="31" cy="52" r="6" fill="#fff"/><circle cx="53" cy="30" r="6" fill="#fff"/><path d="M58 24l10-10M62 36l12-4"/></svg>
    </div>
    <h3>Process Automation</h3>
    <p>Lorem Ipsum is simply dummy text of the printing and typesetting industry. Lorem Ipsum has been the industry's stand.</p>
  </div>
  <div class="sector" style="left:805px">
    <div class="icon">
      <svg width="84" height="84" viewBox="0 0 84 84" fill="none" stroke="#0a84a6" stroke-width="3"><circle cx="20" cy="18" r="7"/><path d="M20 4v4M6 18h4M10 8l3 3M30 8l-3 3"/><path d="M24 34h52l4 34H20z"/><path d="M37 34l-2 34M50 34v34M63 34l2 34M22 45h56M21 56h58"/><path d="M50 68v10M40 78h20"/></svg>
    </div>
    <h3>General Engineering</h3>
    <p>Lorem Ipsum is simply dummy text of the printing and typesetting industry. Lorem Ipsum has been the industry's standard.</p>
  </div>
</section>

<section class="about">
  <h2>About <span class="accent">Torvel Power</span></h2>
  <div class="copy">
    <p>We are the solar experts in the solar kingdom. The KSA (Saudi Arabia) solar market is a promising market with huge potential. The plan is to build 41,000 MW of solar in the coming 20 years, as announced by N.R.A (National Renewables Authority).</p>
    <p>We provide our services, both by our in-house team and associated partners. All together have diversified expertise covering various aspects of solar PV. We cover all technology, market and finance related aspects of solar PV.</p>
  </div>
  <div class="btn" style="left:76px;top:334px;width:167px;height:57px">Know more</div>
  <div class="about-photo" role="img" aria-label="Light bulb shape filled with a solar panel field under blue sky"></div>
</section>

<section class="projects">
  <h2 class="section-title">Latest <span>Projects</span></h2>
  <p class="sub">Renewable Energy, Process Automation and General Engineering</p>
  <div class="card" style="left:93px">
    <div class="photo" role="img" aria-label="Row of solar panels on a green field" style="background:linear-gradient(180deg,#d7e4ee 0%,#6c8fae 45%,#4a6478 75%,#6f8a4e 100%)"></div>
    <div class="title">Project title goes here</div>
  </div>
  <div class="card active" style="left:439px">
    <div class="photo" role="img" aria-label="Solar panels and wind turbines under a deep blue sky" style="background:linear-gradient(180deg,#1d5fb3 0%,#4a8ad4 40%,#2a5a9a 70%,#1b3b6b 100%)"></div>
    <div class="title">Project title goes here</div>
  </div>
  <div class="card" style="left:785px">
    <div class="photo" role="img" aria-label="Worker walking across a large rooftop solar array" style="background:linear-gradient(180deg,#c9c9c9 0%,#9a9a9a 35%,#3c4652 65%,#252c35 100%)"></div>
    <div class="title">Project title goes here</div>
  </div>
</section>

<section class="split">
  <h2 style="left:79px">Our <span class="accent">Training</span></h2>
  <div class="training-photo" role="img" aria-label="Engineers in hard hats standing beside a solar installation"></div>
  <p class="training-text">Lorem Ipsum is simply dummy text of the printing and typesetting industry. Lorem Ipsum has been the industry's standard. simply</p>
  <div class="btn" style="left:76px;top:379px;width:167px;height:57px">Contact us</div>
  <div class="divider"></div>

  <h2 style="left:623px">What our <span class="accent">client say</span></h2>
  <div class="quote" style="top:141px">
    <div class="avatar" role="img" aria-label="Client portrait"></div>
    <blockquote>“ Lorem Ipsum is simply dummy text of the printing and typesetting industry. Lorem Ipsum has been the industry's standard. ”</blockquote>
    <cite>— &nbsp;Client Name</cite>
    <div class="rule"></div>
  </div>
  <div class="quote" style="top:301px">
    <div class="avatar" role="img" aria-label="Client portrait"></div>
    <blockquote>“ Lorem Ipsum is simply dummy text of the printing and typesetting industry. Lorem Ipsum has been the industry's standard. ”</blockquote>
    <cite>— &nbsp;Client Name</cite>
    <div class="rule"></div>
  </div>
</section>

<section class="contact">
  <h2 class="section-title">Contact <span class="accent">Us</span></h2>
  <p class="sub">Send an email</p>
  <div class="field" style="left:122px;top:157px;width:310px;height:50px">Name*</div>
  <div class="field" style="left:444px;top:157px;width:310px;height:50px">Email*</div>
  <div class="field" style="left:766px;top:157px;width:310px;height:50px">Subject*</div>
  <div class="field" style="left:122px;top:222px;width:954px;height:100px">Message*</div>
  <div class="btn">Submit</div>
</section>

<footer class="site-footer">
  <div class="footer-brand"><span class="dot"></span>TORVEL</div>
  <div class="social">
    <span role="img" aria-label="Social link"></span><span role="img" aria-label="Social link"></span><span role="img" aria-label="Social link"></span>
  </div>

  <div class="footer-col" style="left:346px">
    <h4>Usefull links</h4>
    <ul class="links">
      <li>Home</li><li>About</li><li>Services</li><li>Clients</li><li>Projects</li><li>Training</li><li>Career</li><li>Contact</li>
    </ul>
  </div>

  <div class="footer-col newsletter" style="left:611px">
    <h4>Newsletter</h4>
    <p>Would you like to receive exclusive access to articles, white papers and our regular monthly newsletter?</p>
    <div class="email">Enter Email Id</div>
    <div class="btn">Subscribe</div>
  </div>

  <div class="footer-col" style="left:876px">
    <h4>Get in touch</h4>
    <ul class="touch">
      <li>
        <svg width="22" height="20" viewBox="0 0 22 20" fill="none" stroke="#0a84a6" stroke-width="2"><path d="M1 3l6-2 8 2 6-2v16l-6 2-8-2-6 2z"/><path d="M7 1v16M15 3v16"/></svg>
        <div><div class="name">TORVEL POWER</div>Dammar Eastern Province<br>30417 Kingdom of Saudi<br>Arabia</div>
      </li>
      <li>
        <svg width="22" height="20" viewBox="0 0 24 24" fill="none" stroke="#0a84a6" stroke-width="2"><path d="M5 3h4l2 5-3 2a12 12 0 0 0 6 6l2-3 5 2v4a2 2 0 0 1-2 2A17 17 0 0 1 3 5a2 2 0 0 1 2-2z"/></svg>
        info@torvelpower.com
      </li>
      <li>
        <svg width="22" height="18" viewBox="0 0 24 18" fill="none" stroke="#0a84a6" stroke-width="2"><rect x="1" y="1" width="22" height="16" rx="2"/><path d="M1 2l11 8 11-8"/></svg>
        +966135550199
      </li>
    </ul>
  </div>
</footer>

<div class="bottom-bar">©TORVEL POWER - 2017. All Rights Reserved</div>

</body>
</html>
```